A landing page for an exclusive club VELKARDO

We need a fresh, stylish and luxury design for a landing page of an international private club called VELKARDO.

After receiving your first drafts, let me briefly emphasize some important points:
1) Top picture: I would like to see here some good looking intelligent people (not dancing teenagers or smiling couple – because it’s not a pure dating website)
2) Member’s section: the main message of this slide is to communicate the idea of EXCLUSIVITY - the club has exclusive audience (well-educated, intellectual, financially successful people from world-leading universities and well-known companies). I do not want to reveal real members’ profiles on this slide (it’s allowed only in the review section)
3) Event section should not have real future events, just describe event categories.
4) Technology section should communicate the idea of sending REAL presents (a drink or flowers) to a girl via the app. (maybe by using some dynamic elements during the scrolling)
5) Review section – please make it individual design, not a standard one. Please add company’s names and job titles to reviewers.
6) Event section: we will not post actual events, rather some event categories with large attractive pictures.
7) Technical note: We do not have “register” button – people can log in or register only via QN – it’s one button
Let me know if you have any questions. Thank you for participating!

Kind regards,
Teodor Vashkin

Reason: Dear designers, I have to extend the deadline as I did not receive any 5* designs so far. I would like to get a unique design - not a combination of standard blocks for landing pages. I understand the task is difficult, so I decided to give you more time to prepare well-though and original piece of art. Please use the text from the brief and add your ideas. The 3 main messages to communicate are: 1) Member’s section: the main message of this slide is to communicate the idea of EXCLUSIVITY - the club has exclusive audience (well-educated, intellectual, successful people from world-leading universities and well-known companies). I do not want to reveal real members’ profiles on this slide (it’s allowed only in the review section). 2) Event section: the club runs lots of invitation-only events in most exclusive venues. We will not post actual events, but rather some event categories with large attractive pictures and short descriptions. 3) Technology section should communicate the idea of sending REAL presents (a drink or flowers) to a girl via the app. If you can show it by using some dynamic elements during the scrolling it's fantastic! Good luck! I look forward for your creative ideas and art! Kind regards, Teodor Vashkin

Target Market(s)

Alumni of top universities, middle- and top-level managers of large companies, financial professionals (investment bankers), successful entrepreneurs, recognized creative class (fashion designers, models).

Industry/Entity Type

Club

Coding

Coded - Design and coding required

Number of Pages Required

2 page

Font styles to use
Serif
Sans Serif
Other font styles liked:
• Lato, Oswald, Raleway

Requirements
Must have
• Adaptive design (desktop & mobile)
• Elegant and luxury design
• Structure according to the brief
Nice to have
• Dynamic elements/Layers on the landing page
Should not have
• Trivial stock photos.

```html
<!DOCTYPE html>
<html lang="en">
<head>
<meta charset="utf-8">
<title>VELKARDO — Private Club</title>
<link rel="stylesheet" href="https://fonts.googleapis.com/css2?family=Oswald:wght@400;500;700&family=Raleway:ital,wght@0,400;0,500;0,600;0,700;1,400&display=swap">
<style>
:root{
  --teal:#2e9c98;
  --teal-dark:#26857f;
  --tan:#c9986a;
  --ink:#1c1818;
  --night:#231f1f;
  --paper:#f3f2f0;
  --text:#6a6a6a;
  --white:#ffffff;
}
*{margin:0;padding:0;box-sizing:border-box}
html,body{width:1200px;height:2880px;overflow:hidden}
body{background:var(--paper);font-family:"Raleway",sans-serif;color:var(--text);position:relative}
section,header,footer{position:absolute;left:0;width:1200px}
.abs{position:absolute}

/* header */
.site-header{top:0;height:98px;background:var(--white)}
.brand{left:100px;top:10px;width:190px;text-align:center}
.brand-mark{width:44px;height:44px;border:3px solid var(--ink);border-radius:50%;margin:0 auto 6px}
.brand-name{font-family:"Raleway",sans-serif;font-weight:600;font-size:14px;letter-spacing:9px;color:var(--ink)}
.login-btn{left:883px;top:33px;width:138px;height:28px;background:#3b5a96;border-radius:3px;color:var(--white);font-size:12px;font-weight:500;line-height:28px;text-align:center}
.menu{left:1044px;top:38px;font-size:13px;font-weight:700;color:var(--ink);display:flex;align-items:center;gap:6px}
.menu svg{display:block}

/* hero */
.hero{top:98px;height:513px;background:var(--teal);overflow:hidden}
.hero-title{left:98px;top:130px;font-family:"Oswald",sans-serif;font-weight:500;font-size:29px;line-height:1.2;color:var(--white)}
.hero-lead{left:98px;top:174px;width:600px;font-size:18.5px;line-height:29px;color:var(--white)}
.hero-btn{top:282px;height:42px;background:var(--ink);border:2px solid #555;color:#e8e8e8;font-size:11px;font-weight:600;line-height:38px;text-align:center;letter-spacing:.5px}
.hero-btn.video{left:100px;width:140px}
.hero-btn.join{left:282px;width:140px;color:var(--tan)}
.hero-art{left:676px;top:4px;width:482px;height:480px;border-radius:50%;background:radial-gradient(circle at 50% 50%,#1f6f6b 0 55%,#f3b57a 56% 62%,#6cc1bd 63% 100%)}
.dots{left:556px;top:430px;display:flex;gap:17px}
.dots span{width:9px;height:9px;border-radius:50%;background:var(--white)}
.dots span.on{background:var(--ink)}

/* common section heading */
.heading{left:0;width:1200px;text-align:center}
.heading h2{font-family:"Oswald",sans-serif;font-weight:500;font-size:33px;letter-spacing:10px;color:var(--ink);line-height:1}
.ornament{display:block;margin:0 auto}
.heading.light h2{color:var(--white)}

/* membership */
.membership{top:611px;height:647px}
.phone{left:165px;top:112px;width:255px;height:480px;border-radius:34px;background:linear-gradient(180deg,#4a4545,#2c2828);box-shadow:0 22px 18px -14px rgba(0,0,0,.25)}
.phone-screen{position:absolute;left:20px;top:68px;width:215px;height:346px;background:linear-gradient(180deg,#6d5a50,#b89a86 50%,#56504c)}
.timeline-v{left:470px;top:186px;width:1px;height:170px;background:var(--tan)}
.point{width:8px;height:8px;border-radius:50%;background:var(--tan);left:466px}
.bullet{left:504px;width:590px;font-size:14px;line-height:24px;color:var(--text)}
.features{left:484px;top:432px;display:flex;gap:0}
.feature{width:162px;text-align:center;font-size:14px;font-weight:500;color:#555}
.feature svg{display:block;margin:0 auto 12px;height:62px}
.cta{left:505px;top:548px;width:136px;height:40px;background:var(--ink);border:2px solid var(--tan);color:var(--white);font-family:"Oswald",sans-serif;font-size:15px;line-height:36px;text-align:center}
.rule{left:200px;top:640px;width:800px;height:1px;background:#dcdad6}

/* events */
.events{top:1258px;height:576px}
.track{left:92px;top:340px;width:1016px;height:2px;background:var(--tan)}
.track-end{width:16px;height:16px;border-radius:50%;background:var(--tan);top:333px}
.chev{top:326px;font-size:22px;color:var(--ink);font-weight:700}
.stem{width:1px;background:var(--tan)}
.event-photo{width:80px;height:80px;border-radius:50%;border:3px solid var(--teal);background:radial-gradient(circle,#7a5a48,#2d2420)}
.event-card{min-height:90px;background:var(--ink);color:var(--white);padding:12px 20px 14px}
.event-card::before{content:"";position:absolute;left:-12px;top:14px;border:7px solid transparent;border-right:6px solid var(--ink)}
.event-card h3{font-family:"Raleway",sans-serif;font-weight:700;font-size:15px;margin-bottom:6px}
.event-card p{font-size:12px;line-height:21px;color:#e6e6e6}
.event-date{font-family:"Oswald",sans-serif;font-size:13px;color:var(--teal)}

/* technology */
.technology{top:1834px;height:364px;background:linear-gradient(110deg,#5a4a42 0%,#3f3a38 45%,#56504b 75%,#3a3634 100%)}
.tech-lead{left:0;top:172px;width:1200px;text-align:center;font-size:14.5px;line-height:25px;color:#f0f0f0}
.download{left:418px;top:260px;display:flex;align-items:center;gap:24px;font-size:14px;color:var(--white)}
.store-badge{width:136px;height:44px;border-radius:6px;background:#111;border:1px solid #888}

/* review */
.review{top:2198px;height:455px}
.quote{left:0;top:150px;width:1200px;text-align:center;font-style:italic;font-size:23px;line-height:38px;color:#7a7a7a}
.avatar{left:556px;top:245px;width:86px;height:86px;border-radius:50%;border:3px solid var(--white);background:linear-gradient(160deg,#c58a5a,#e8c3a3)}
.reviewer{left:0;top:337px;width:1200px;text-align:center;line-height:1.3}
.reviewer strong{display:block;font-size:22px;font-weight:700;color:#555}
.reviewer span{font-size:15px;font-weight:600;color:#555}
.review-dots{left:577px;top:415px;display:flex;gap:4px}
.review-dots span{width:12px;height:12px;background:var(--teal)}
.review-dots span.off{background:var(--white);border:1px solid #ddd}
.quote-mark{left:985px;top:250px;font-family:Georgia,serif;font-size:330px;line-height:1;color:#e2e1df}

/* footer */
.site-footer{top:2653px;height:179px;background:var(--night)}
.footer-brand{left:0;top:18px;width:1200px;text-align:center}
.footer-brand .brand-mark{border-color:var(--white);width:40px;height:40px}
.footer-brand .brand-name{color:var(--white);font-size:13px}
.social{left:562px;top:102px;display:flex;gap:10px}
.social span{width:16px;height:16px;background:var(--white);border-radius:2px}
.footer-nav{left:0;top:139px;width:1200px;display:flex;justify-content:center;gap:34px;font-size:13px;color:var(--white)}
.copyright{top:2832px;height:48px;background:#151212;text-align:center;line-height:48px;font-size:12px;color:#ddd}
</style>
</head>
<body>

<header class="site-header">
  <div class="brand abs"><div class="brand-mark"></div><div class="brand-name">VELKARDO</div></div>
  <div class="login-btn abs">Log in with QN</div>
  <div class="menu abs">MENU
    <svg width="13" height="11" viewBox="0 0 13 11"><rect y="0" width="13" height="2" fill="#1c1818"/><rect y="4.5" width="13" height="2" fill="#1c1818"/><rect y="9" width="13" height="2" fill="#1c1818"/></svg>
  </div>
</header>

<section class="hero">
  <h1 class="hero-title abs">WELCOME TO VELKARDO</h1>
  <p class="hero-lead abs">VELKARDO Club is an international circle of trust which brings together exceptional people committed to building lasting relationships - personal or business</p>
  <div class="hero-btn video abs">PLAY VIDEO ▸</div>
  <div class="hero-btn join abs">WANT TO JOIN ●</div>
  <div class="hero-art abs" role="img" aria-label="Illustration of people seated around a round meeting table with laptops and papers, seen from above"></div>
  <div class="dots abs"><span class="on"></span><span></span><span></span><span></span></div>
</section>

<section class="membership">
  <div class="heading abs" style="top:30px">
    <svg class="ornament" width="140" height="10" viewBox="0 0 140 10"><line x1="0" y1="5" x2="64" y2="5" stroke="#c9986a"/><line x1="76" y1="5" x2="140" y2="5" stroke="#c9986a"/><circle cx="70" cy="5" r="2" fill="#c9986a"/></svg>
    <h2 style="margin:14px 0">MEMBERSHIP</h2>
    <svg class="ornament" width="140" height="10" viewBox="0 0 140 10"><line x1="0" y1="5" x2="64" y2="5" stroke="#c9986a"/><line x1="76" y1="5" x2="140" y2="5" stroke="#c9986a"/><circle cx="70" cy="5" r="2" fill="#c9986a"/></svg>
  </div>

  <div class="phone abs" role="img" aria-label="Smartphone showing a grid of club member portraits">
    <div class="phone-screen"></div>
  </div>

  <div class="timeline-v abs"></div>
  <div class="point abs" style="top:186px"></div>
  <div class="point abs" style="top:252px"></div>
  <div class="point abs" style="top:335px"></div>
  <p class="bullet abs" style="top:180px">Candidates apply for membership on VELKARDO's website and mobile app. All applications are reviewed by our international committee of trustees.</p>
  <p class="bullet abs" style="top:246px">To join the Club applicants need to satisfy the Club's requirements: our carefully selected members come from the world's leading universities, top-tier companies, governments and successful family businesses.</p>
  <p class="bullet abs" style="top:329px">Club members participate in regular private events and weekend trips, discover, meet and socialise with similar high-calibre people and receive exclusive privileges from inspirational brands.</p>

  <div class="features abs">
    <div class="feature">
      <svg viewBox="0 0 64 58" width="64"><path d="M32 56 C10 40 2 28 2 17 C2 8 9 2 17 2 C24 2 29 6 32 11 C35 6 40 2 47 2 C55 2 62 8 62 17 C62 28 54 40 32 56Z" fill="#2e9c98"/></svg>Personal</div>
    <div class="feature">
      <svg viewBox="0 0 64 58" width="64"><rect x="22" y="2" width="20" height="12" rx="3" fill="none" stroke="#2e9c98" stroke-width="5"/><rect x="2" y="12" width="60" height="44" rx="5" fill="#2e9c98"/><rect x="14" y="12" width="4" height="44" fill="#f3f2f0"/><rect x="46" y="12" width="4" height="44" fill="#f3f2f0"/></svg>Business</div>
    <div class="feature">
      <svg viewBox="0 0 64 58" width="64"><ellipse cx="24" cy="22" rx="22" ry="18" fill="#2e9c98"/><path d="M10 36 L6 48 L20 38Z" fill="#2e9c98"/><ellipse cx="44" cy="36" rx="18" ry="14" fill="#2e9c98" stroke="#f3f2f0" stroke-width="3"/><path d="M52 47 L58 56 L46 49Z" fill="#2e9c98"/><circle cx="36" cy="36" r="2.5" fill="#fff"/><circle cx="44" cy="36" r="2.5" fill="#fff"/><circle cx="52" cy="36" r="2.5" fill="#fff"/></svg>Same People</div>
    <div class="feature">
      <svg viewBox="0 0 64 58" width="64"><circle cx="32" cy="14" r="11" fill="#2e9c98"/><path d="M14 56 C14 36 50 36 50 56Z" fill="#2e9c98"/><circle cx="12" cy="22" r="8" fill="#2e9c98"/><path d="M0 50 C0 36 22 34 22 42 L18 50Z" fill="#2e9c98"/><circle cx="52" cy="22" r="8" fill="#2e9c98"/><path d="M64 50 C64 36 42 34 42 42 L46 50Z" fill="#2e9c98"/></svg>New Friends</div>
  </div>
  <div class="cta abs">Get a membership</div>
  <div class="rule abs"></div>
</section>

<section class="events">
  <div class="heading abs" style="top:36px">
    <svg class="ornament" width="140" height="10" viewBox="0 0 140 10"><line x1="0" y1="5" x2="64" y2="5" stroke="#c9986a"/><line x1="76" y1="5" x2="140" y2="5" stroke="#c9986a"/><circle cx="70" cy="5" r="2" fill="#c9986a"/></svg>
    <h2 style="margin:14px 0">VELKARDO EVENTS</h2>
    <svg class="ornament" width="140" height="10" viewBox="0 0 140 10"><line x1="0" y1="5" x2="64" y2="5" stroke="#c9986a"/><line x1="76" y1="5" x2="140" y2="5" stroke="#c9986a"/><circle cx="70" cy="5" r="2" fill="#c9986a"/></svg>
  </div>

  <div class="track abs"></div>
  <div class="track-end abs" style="left:84px"></div>
  <div class="track-end abs" style="left:1100px"></div>
  <div class="chev abs" style="left:46px">«</div>
  <div class="chev abs" style="left:1140px">»</div>

  <div class="stem abs" style="left:138px;top:262px;height:80px"></div>
  <div class="event-photo abs" style="left:100px;top:184px" role="img" aria-label="Photo of alumni at a meetup"></div>
  <div class="event-card abs" style="left:208px;top:185px;width:347px">
    <h3>ALUMNI MEETUPS</h3>
    <p>VELKARDO's events bring together people based on their professional occupation, education, and interests.</p>
  </div>
  <div class="event-date abs" style="left:228px;top:288px">JUL 27</div>

  <div class="stem abs" style="left:683px;top:262px;height:80px"></div>
  <div class="event-photo abs" style="left:645px;top:184px" role="img" aria-label="Photo of guests at a private viewing"></div>
  <div class="event-card abs" style="left:752px;top:185px;width:347px">
    <h3>PRIVATE VIEWINGS</h3>
    <p>VELKARDO's events bring together people based on their professional occupation, education, and interests.</p>
  </div>
  <div class="event-date abs" style="left:773px;top:288px">JUL 29</div>

  <div class="stem abs" style="left:411px;top:342px;height:84px"></div>
  <div class="event-photo abs" style="left:372px;top:424px;background:radial-gradient(circle,#b0472f,#3a1a14)" role="img" aria-label="Photo from a theatre night"></div>
  <div class="event-card abs" style="left:480px;top:426px;width:347px">
    <h3>THEATRE NIGHTS</h3>
    <p>VELKARDO's events bring together people based on their professional occupation, education, and interests.</p>
  </div>
  <div class="event-date abs" style="left:502px;top:530px">AUG 10</div>
</section>

<section class="technology" role="img" aria-label="Background photo of a hand holding a smartphone over a café table with flowers">
  <div class="heading light abs" style="top:68px">
    <svg class="ornament" width="140" height="10" viewBox="0 0 140 10"><line x1="0" y1="5" x2="64" y2="5" stroke="#fff"/><line x1="76" y1="5" x2="140" y2="5" stroke="#fff"/><circle cx="70" cy="5" r="2" fill="#fff"/></svg>
    <h2 style="margin:14px 0">POWERFULL TECHNOLOGY</h2>
    <svg class="ornament" width="140" height="10" viewBox="0 0 140 10"><line x1="0" y1="5" x2="64" y2="5" stroke="#fff"/><line x1="76" y1="5" x2="140" y2="5" stroke="#fff"/><circle cx="70" cy="5" r="2" fill="#fff"/></svg>
  </div>
  <p class="tech-lead abs">Our State of the art mobile app helps members get togrther,interact at events,Discover people<br>nearby and even receive real presents.</p>
  <div class="download abs">Click here to download our app <span class="store-badge"></span></div>
</section>

<section class="review">
  <div class="heading abs" style="top:36px">
    <svg class="ornament" width="140" height="10" viewBox="0 0 140 10"><line x1="0" y1="5" x2="64" y2="5" stroke="#c9986a"/><line x1="76" y1="5" x2="140" y2="5" stroke="#c9986a"/><circle cx="70" cy="5" r="2" fill="#c9986a"/></svg>
    <h2 style="margin:14px 0">CLUB MEMBERS REVIEW</h2>
    <svg class="ornament" width="140" height="10" viewBox="0 0 140 10"><line x1="0" y1="5" x2="64" y2="5" stroke="#c9986a"/><line x1="76" y1="5" x2="140" y2="5" stroke="#c9986a"/><circle cx="70" cy="5" r="2" fill="#c9986a"/></svg>
  </div>
  <div class="quote-mark abs">&#8220;</div>
  <p class="quote abs">" Lorem ipsum dolor sit amet, consectetuer adipiscing elit. Aenean<br>commodo ligula eget dolor. "</p>
  <div class="avatar abs" role="img" aria-label="Portrait of the reviewer"></div>
  <div class="reviewer abs"><strong>Mara Delling</strong><span>CEO - Northwind Airways</span></div>
  <div class="review-dots abs"><span></span><span class="off"></span><span></span></div>
</section>

<footer class="site-footer">
  <div class="footer-brand abs"><div class="brand-mark"></div><div class="brand-name">VELKARDO</div></div>
  <div class="social abs"><span></span><span></span><span></span></div>
  <nav class="footer-nav abs">
    <span>Home</span><span>Privileges</span><span>Contacts</span><span>Partners</span><span>Media</span><span>User agreement</span><span>Confidently</span><span>FAQ</span>
  </nav>
</footer>
<div class="copyright abs" style="left:0;width:1200px">Copyright © 2016 VELKARDO.All rights received</div>

</body>
</html>
```